Dennis K. Halvorsen stationery and new logo

Create Word template stationery, with a logo, for a Forensic Psychiatry business.

The stationery must include contact info (see below)

The logo should include images similar to (but not necessarily identical to) the ones in the uploaded document. They are the scales of justice and the caduceus, or staff, associated with medicine.

Target Market(s)

consumers of forensic psychiatry (usually lawyers and their clients)

Industry/Entity Type

Mental Health

Logo Text

Dennis K. Halvorsen, MD, DLFAPA

Font styles to use
Serif

Colors

Designer to choose colors to be used in the design.

Requirements
Must have
• Forensic Psychiatry
• 715 N. Maple Street
• R Building
• West Ashford, PA 19804
• (484) 555-3172
Nice to have
• Conservative color scheme

```html
<!DOCTYPE html>
<html lang="en">
<head>
<meta charset="utf-8">
<title>Dennis K. Halvorsen — Stationery</title>
<link href="https://fonts.googleapis.com/css2?family=Gelasio:wght@400;500&family=Source+Sans+3:wght@400;600&display=swap" rel="stylesheet">
<style>
  :root {
    --navy: #0c3f6e;
    --backdrop: #d1d1d3;
    --paper: #ffffff;
    --body-grey: #a9a9a9;
    --ink: #222222;
    --ghost: #e6e6e8;
  }
  html, body { margin: 0; padding: 0; overflow: hidden; }
  body { width: 1200px; height: 960px; background: var(--backdrop); position: relative; }
  .serif { font-family: "Gelasio", Georgia, serif; }
  .sans { font-family: "Source Sans 3", Arial, sans-serif; }

  .mark { position: absolute; display: flex; flex-direction: column; align-items: center; justify-content: center; gap: 6px; text-align: center; }
  .mark .dot { border-radius: 50%; background: var(--navy); }
  .mark .mark-name { font-family: "Gelasio", Georgia, serif; color: var(--navy); white-space: nowrap; }

  /* hero logo */
  .hero-mark { left: 780px; top: 70px; width: 188px; height: 170px; }
  .hero-mark .dot { width: 64px; height: 64px; }
  .hero-mark .mark-name { font-size: 18px; }
  .hero-name { position: absolute; left: 600px; width: 548px; text-align: center; color: var(--navy); font-family: "Gelasio", Georgia, serif; margin: 0; font-weight: 400; }
  .hero-name.line1 { top: 246px; font-size: 44px; }
  .hero-name.line2 { top: 304px; font-size: 35px; }

  /* letterhead */
  .letterhead { position: absolute; left: 41px; top: 253px; width: 524px; height: 677px; background: var(--paper); }
  .letterhead .mark { left: 212px; top: 18px; width: 100px; height: 60px; gap: 3px; }
  .letterhead .mark .dot { width: 26px; height: 26px; }
  .letterhead .mark .mark-name { font-size: 9px; }
  .lh-name { position: absolute; left: 0; width: 100%; text-align: center; color: var(--navy); font-family: "Gelasio", Georgia, serif; margin: 0; }
  .lh-name.line1 { top: 81px; font-size: 15px; }
  .lh-name.line2 { top: 102px; font-size: 12px; font-weight: 500; }
  .salutation { position: absolute; left: 44px; top: 187px; font-size: 9.5px; color: var(--body-grey); margin: 0; }
  .letter-body { position: absolute; left: 33px; top: 229px; width: 458px; color: var(--body-grey); font-size: 9.7px; line-height: 12.2px; text-align: justify; }
  .letter-body p { margin: 0 0 12.4px; }
  .letter-body p:first-child { text-indent: 31px; }
  .contact { position: absolute; font-size: 8px; line-height: 10.8px; color: var(--ink); margin: 0; }
  .contact .accent { color: var(--navy); font-weight: 600; }
  .letterhead .contact { left: 33px; top: 604px; }

  /* envelope back */
  .envelope-back { position: absolute; left: 600px; top: 422px; width: 555px; height: 246px; background: var(--paper); }
  .flap { position: absolute; left: 0; top: 0; width: 100%; height: 55px; background: var(--navy); border-radius: 0 0 24px 24px; }
  .flap .mark { left: 237px; top: 6px; width: 80px; height: 44px; gap: 3px; }
  .flap .mark .dot { width: 22px; height: 22px; background: var(--paper); }
  .flap .mark .mark-name { color: var(--paper); font-size: 8px; }

  /* envelope front */
  .envelope-front { position: absolute; left: 600px; top: 684px; width: 555px; height: 246px; background: var(--paper); overflow: hidden; }
  .envelope-front .mark.small { left: 16px; top: 16px; width: 84px; height: 48px; gap: 3px; }
  .envelope-front .mark.small .dot { width: 24px; height: 24px; }
  .envelope-front .mark.small .mark-name { font-size: 8px; }
  .ef-name { position: absolute; left: 0; width: 132px; text-align: center; color: var(--navy); font-family: "Gelasio", Georgia, serif; margin: 0; }
  .ef-name.line1 { top: 64px; font-size: 12px; }
  .ef-name.line2 { top: 80px; font-size: 10px; font-weight: 500; }
  .envelope-front .contact { left: 21px; top: 167px; line-height: 10.6px; }
  .envelope-front .contact .gap { display: block; height: 3px; }
  .ghost-mark { left: 296px; top: 10px; width: 234px; height: 214px; gap: 10px; }
  .ghost-mark .dot { width: 110px; height: 110px; background: var(--ghost); }
  .ghost-mark .mark-name { color: var(--ghost); font-size: 20px; }
</style>
</head>
<body>

  <div class="mark hero-mark" aria-label="Dennis K. Halvorsen mark">
    <span class="dot"></span>
    <span class="mark-name">Dennis K. Halvorsen</span>
  </div>
  <h1 class="hero-name line1">Dennis K. Halvorsen</h1>
  <p class="hero-name line2">MD, DLFAPA</p>

  <section class="letterhead">
    <div class="mark">
      <span class="dot"></span>
      <span class="mark-name">Dennis K. Halvorsen</span>
    </div>
    <p class="lh-name line1">Dennis K. Halvorsen</p>
    <p class="lh-name line2">MD, DLFAPA</p>

    <p class="salutation sans">Dear Sir</p>
    <div class="letter-body sans">
      <p>Lorem ipsum dolor sit amet, consectetur adipiscing elit. Integer eu odio mattis, pulvinar turpis quis, faucibus nisl. Proin feugiat, erat vitae cursus pharetra, enim est semper ligula, in malesuada orci nisl et diam. Etiam elementum metus ac fringilla vulputate. Etiam mattis ligula sed ante mollis bibendum. Orci varius natoque penatibus et magnis dis parturient montes, nascetur ridiculus mus.</p>
      <p>Ut nibh augue, blandit ac orci ac, rutrum congue enim. Suspendisse gravida vulputate felis, quis interdum orci tincidunt quis. Praesent imperdiet maximus neque. Mauris ut dui enim. Nullam at efficitur elit. Donec ante ipsum, fermentum at lectus vel, blandit vulputate ante. Proin luctus suscipit diam id vestibulum. Morbi malesuada id mauris eget ullamcorper.</p>
      <p>Donec varius orci purus, vitae aliquam libero volutpat id. Integer sed imperdiet libero. Aliquam accumsan, risus sit amet ornare consectetur, turpis felis dictum justo, non rhoncus mauris dui sed velit. Pellentesque habitant morbi tristique senectus et netus et malesuada fames ac turpis egestas. Pellentesque tincidunt vitae ligula nec imperdiet. Donec sed congue enim. Nullam elementum faucibus nulla nec vestibulum. Sed at tempor ligula. In quis vulputate nunc. Integer at gravida lacus, ac tristique risus. Sed at vulputate nulla.</p>
      <p>Praesent blandit nunc eu efficitur commodo. In tempor nisi ex, vel venenatis ante vestibulum a. Duis vestibulum nibh a erat sagittis, nec euismod lorem varius. Nam ultricies turpis sed justo sollicitudin volutpat. Morbi sed mollis eros. Sed quis tortor id enim vehicula porttitor. Curabitur non aliquam ex. Phasellus dignissim fermentum elit, at finibus ligula mattis eget.</p>
    </div>

    <p class="contact sans">
      <span class="accent">Forensic Psychiatry</span><br>
      715 N. Maple Street, R Building<br>
      West Ashford, PA 19804<br>
      <span class="accent">(484) 555-3172</span>
    </p>
  </section>

  <section class="envelope-back">
    <div class="flap">
      <div class="mark">
        <span class="dot"></span>
        <span class="mark-name">Dennis K. Halvorsen</span>
      </div>
    </div>
  </section>

  <section class="envelope-front">
    <div class="mark ghost-mark" aria-hidden="true">
      <span class="dot"></span>
      <span class="mark-name">Dennis K. Halvorsen</span>
    </div>
    <div class="mark small">
      <span class="dot"></span>
      <span class="mark-name">Dennis K. Halvorsen</span>
    </div>
    <p class="ef-name line1">Dennis K. Halvorsen</p>
    <p class="ef-name line2">MD, DLFAPA</p>
    <p class="contact sans">
      Forensic Psychiatry<br>
      715 N. Maple Street<br>
      R Building<br>
      West Ashford, PA 19804<br>
      <span class="gap"></span>(484) 555-3172
    </p>
  </section>

</body>
</html>
```